Software as a Service to manage Home Care Management

We need a web site designed for Home Care Management Software as a Service product, that facilitates Home Care organizations to manage and schedule carers to visit client homes. We want a modern look and feel using our existing logo.

Target Market(s)

Home Care Management organizations. Product is similar to: https://kelvantro.co/

Coding

Coded - Design and coding required

Number of Pages Required

3 page

```html
<!DOCTYPE html>
<html lang="en">
<head>
<meta charset="utf-8">
<title>Visitline – Home Care Management Software</title>
<link href="https://fonts.googleapis.com/css2?family=Roboto:wght@300;400;500&display=swap" rel="stylesheet">
<style>
:root{
  --pink:#ff4182;
  --dark:#222222;
  --ink:#1d1d1d;
  --muted:#555555;
  --line:#cfcfcf;
  --white:#ffffff;
}
*{box-sizing:border-box;margin:0;padding:0}
html,body{width:1200px;height:3735px;overflow:hidden}
body{position:relative;font-family:'Roboto',sans-serif;color:var(--ink);background:var(--white)}
.abs{position:absolute}
.btn{position:absolute;background:var(--pink);color:var(--white);border-radius:20px;display:flex;align-items:center;justify-content:center;font-size:16px;font-weight:400}

/* header */
.site-header{position:absolute;left:0;top:0;width:1200px;height:102px;background:var(--white)}
.brand{position:absolute;display:flex;align-items:center;gap:12px}
.brand-mark{width:34px;height:34px;border-radius:50%;background:var(--pink)}
.brand-name{font-size:32px;font-weight:400;letter-spacing:1px;color:#444}
.nav{position:absolute;left:664px;top:41px;display:flex;gap:17px;font-size:13px;color:var(--ink)}

/* hero */
.hero-photo{position:absolute;left:0;top:102px;width:1200px;height:700px}
.hero-title{position:absolute;left:150px;top:258px;width:900px;text-align:center;color:var(--white);font-size:58px;font-weight:400;line-height:68px}
.hero-text{position:absolute;left:222px;top:404px;width:756px;text-align:center;color:var(--white);font-size:20px;line-height:26px;font-weight:300}

/* features */
.section-title{position:absolute;left:0;top:878px;width:1200px;text-align:center;font-size:27px;font-weight:400}
.feature-icon{position:absolute;width:146px;height:146px}
.feature-text{position:absolute;width:262px;text-align:center;font-size:9.5px;line-height:12.5px;color:#333}

/* stats */
.stat{position:absolute;width:240px;text-align:center;color:var(--white)}
.stat-label{font-size:17px;font-weight:300}
.stat-value{font-size:31px;font-weight:300;margin-top:6px}
.stat-rule{width:68px;height:2px;background:var(--white);margin:14px auto 0}

/* optimised */
.promo-art{position:absolute;left:140px;top:1740px;width:380px;height:375px;border-radius:8px;background:linear-gradient(160deg,#fbe3e9,#f6d9c6 60%,#efe6e3)}
.promo-title{position:absolute;left:600px;top:1736px;font-size:50px;font-weight:400;line-height:62px;color:#333}
.promo-list{position:absolute;left:602px;top:1878px;width:530px;list-style:none;font-size:20.5px;line-height:26px;color:#333;font-weight:300}
.promo-list li{position:relative;padding-left:30px}
.promo-list li::before{content:"";position:absolute;left:6px;top:10px;width:7px;height:7px;border-radius:50%;background:var(--pink)}

/* service band */
.service-photo{position:absolute;left:0;top:2233px;width:1200px;height:830px}
.service-icon{position:absolute;width:140px;height:140px}
.service-text{position:absolute;width:262px;text-align:center;font-size:9.5px;line-height:12.5px;color:var(--white)}

/* contact */
.contact-title{position:absolute;left:200px;top:3160px;width:307px;text-align:right;font-size:27px;font-weight:400}
.contact-text{position:absolute;left:170px;top:3222px;width:337px;text-align:right;font-size:17px;line-height:21.5px;color:#333}
.contact-phone{position:absolute;left:200px;top:3384px;width:307px;text-align:right;font-size:17px;color:#333}
.field{position:absolute;left:555px;width:468px;height:40px;border:1px solid var(--line);border-radius:7px;font-size:12px;font-style:italic;color:#777;padding:15px 14px 0}
.field.tall{height:98px;padding-top:12px}

/* footer */
.site-footer{position:absolute;left:0;top:3573px;width:1200px;height:162px;background:var(--dark);color:var(--white)}
.footer-brand .brand-name{font-size:24px;color:var(--white)}
.footer-brand .brand-mark{width:28px;height:28px}
.footer-contact{position:absolute;font-size:14px;line-height:17px}
.footer-contact .label{color:var(--pink)}
.footer-rule{position:absolute;left:30px;top:82px;width:1140px;height:1px;background:#444}
.footer-col{position:absolute;top:100px;font-size:8.5px;line-height:11px;color:#bbb}
.social{position:absolute;top:98px;width:20px;height:20px;border-radius:50%;background:var(--pink)}
.legal{position:absolute;left:700px;top:146px;width:470px;text-align:right;font-size:8.5px;color:#bbb}
</style>
</head>
<body>

<header class="site-header">
  <div class="brand" style="left:28px;top:30px">
    <span class="brand-mark"></span>
    <span class="brand-name">VISITLINE</span>
  </div>
  <nav class="nav">
    <span>Home</span><span>Product</span><span>Pricing</span><span>Blog</span><span>FAQ</span><span>Contact us</span>
  </nav>
  <div class="btn" style="left:1025px;top:29px;width:135px;height:38px">Free Demo</div>
</header>

<svg class="hero-photo" viewBox="0 0 1200 700" role="img" aria-label="Photo of an older couple reviewing care notes at a laptop in a home kitchen">
  <defs>
    <linearGradient id="heroGrad" x1="0" y1="0" x2="1" y2="1">
      <stop offset="0" stop-color="#6e6257"/>
      <stop offset=".5" stop-color="#8a7a6c"/>
      <stop offset="1" stop-color="#5e4a42"/>
    </linearGradient>
  </defs>
  <polygon points="0,0 1200,0 1200,648 600,693 0,648" fill="url(#heroGrad)"/>
  <polygon points="0,0 1200,0 1200,648 600,693 0,648" fill="#000" opacity=".18"/>
</svg>
<h1 class="hero-title">HOME CARE MANAGEMENT<br>SOFTWARE</h1>
<p class="hero-text">Lorem ipsum dolor sit amet, consectetur adipiscing elit. Cras lacinia hendrerit leo tincidunt dapibus. Fusce efficitur sollicitudin blandit. Phasellus dolor dolor, luctus tempus rhoncus eu, luctus non arcu. Ut purus arcu, consectetur id sem et, aliquet tincidunt diam.</p>

<h2 class="section-title">LOREM IPSUM DOLOR SIT</h2>

<svg class="feature-icon" style="left:163px;top:985px" viewBox="0 0 146 146" fill="none" stroke="#111" stroke-width="3">
  <circle cx="73" cy="73" r="71"/>
  <path d="M36 70 L73 40 L110 70"/><path d="M46 62 V108 H100 V62"/><path d="M90 48 V40 H98 V55"/>
  <path d="M73 95 C55 83 58 70 66 70 C70 70 73 74 73 76 C73 74 76 70 80 70 C88 70 91 83 73 95Z"/>
</svg>
<svg class="feature-icon" style="left:527px;top:985px" viewBox="0 0 146 146" fill="none" stroke="#111" stroke-width="3">
  <circle cx="73" cy="73" r="71"/>
  <rect x="36" y="42" width="74" height="52" rx="3"/><path d="M60 108 H86 M73 94 V108"/>
  <circle cx="73" cy="60" r="9"/><path d="M56 92 C56 78 90 78 90 92"/>
</svg>
<svg class="feature-icon" style="left:891px;top:985px" viewBox="0 0 146 146" fill="none" stroke="#111" stroke-width="3">
  <circle cx="73" cy="73" r="71"/>
  <rect x="46" y="34" width="44" height="78" rx="5"/><path d="M58 42 H78"/>
  <path d="M56 78 L64 70 L72 80 L66 86 C70 94 76 98 80 100 L86 94 L94 102 L86 110"/>
  <rect x="86" y="56" width="22" height="22" rx="3"/><path d="M97 61 V73 M91 67 H103"/>
</svg>

<p class="feature-text" style="left:105px;top:1178px">Plan every visit, match the right carer to each client and keep schedules current from one clear dashboard. Staff get instant updates on any device, so families always know who is coming and when care happens.</p>
<p class="feature-text" style="left:469px;top:1178px">Plan every visit, match the right carer to each client and keep schedules current from one clear dashboard. Staff get instant updates on any device, so families always know who is coming and when care happens.</p>
<p class="feature-text" style="left:834px;top:1178px">Plan every visit, match the right carer to each client and keep schedules current from one clear dashboard. Staff get instant updates on any device, so families always know who is coming and when care happens.</p>

<svg class="abs" style="left:0;top:1320px" width="1200" height="292" viewBox="0 0 1200 292">
  <polygon points="0,0 600,63 1200,0 1200,228 600,290 0,228" fill="var(--pink)"/>
</svg>
<div class="stat" style="left:115px;top:1437px"><div class="stat-label">Users</div><div class="stat-value">70,000+</div><div class="stat-rule"></div></div>
<div class="stat" style="left:482px;top:1437px"><div class="stat-label">Care hours</div><div class="stat-value">110,000+</div><div class="stat-rule"></div></div>
<div class="stat" style="left:845px;top:1437px"><div class="stat-label">Happiness</div><div class="stat-value">96%</div><div class="stat-rule"></div></div>

<div class="promo-art" role="img" aria-label="Illustration of hands holding a phone showing a care app chat"></div>
<h2 class="promo-title">Optimised Home Care<br>Software</h2>
<ul class="promo-list">
  <li>Lorem ipsum dolor sit amet, consectetur adipiscing elit. Cras lacinia hendrerit leo tincidunt dapibus.</li>
  <li>Fusce efficitur sollicitudin blandit. Phasellus dolor dolor, luctus tempus rhoncus eu, luctus non arcu. Ut</li>
  <li>purus arcu, consectetur id sem et, aliquet tincidunt diam.</li>
</ul>
<div class="btn" style="left:598px;top:2057px;width:134px;height:37px;font-size:16px">Try now!</div>

<svg class="service-photo" viewBox="0 0 1200 830" role="img" aria-label="Photo of a smiling older couple sharing breakfast and looking at a phone">
  <defs>
    <linearGradient id="svcGrad" x1="0" y1="0" x2="1" y2="1">
      <stop offset="0" stop-color="#4f5a6c"/>
      <stop offset=".55" stop-color="#6b7282"/>
      <stop offset="1" stop-color="#8d8478"/>
    </linearGradient>
  </defs>
  <polygon points="0,0 600,40 1200,0 1200,762 600,825 0,762" fill="url(#svcGrad)"/>
  <polygon points="0,0 600,40 1200,0 1200,762 600,825 0,762" fill="#1c2230" opacity=".3"/>
</svg>

<svg class="service-icon" style="left:143px;top:2570px" viewBox="0 0 140 140" fill="none" stroke="#fff" stroke-width="4">
  <rect x="8" y="16" width="110" height="92" rx="6"/><path d="M8 38 H118"/>
  <path d="M30 6 V26 M56 6 V26 M82 6 V26 M106 6 V26"/>
  <rect x="20" y="50" width="20" height="18"/><rect x="50" y="50" width="20" height="18"/><rect x="80" y="50" width="20" height="18"/>
  <rect x="20" y="78" width="20" height="18"/><rect x="50" y="78" width="20" height="18"/>
  <circle cx="106" cy="106" r="24" fill="#4f5a6c"/><path d="M106 92 V106 L116 114"/>
</svg>
<svg class="service-icon" style="left:535px;top:2570px" viewBox="0 0 140 140" fill="none" stroke="#fff" stroke-width="4">
  <rect x="30" y="16" width="84" height="118" rx="6"/>
  <path d="M44 6 V26 M60 6 V26 M76 6 V26 M92 6 V26"/>
  <path d="M46 44 H100 M46 60 H100 M46 76 H100 M46 92 H100 M46 108 H80"/>
  <path d="M4 100 L38 134 L48 124 L14 90 Z"/>
</svg>
<svg class="service-icon" style="left:900px;top:2570px" viewBox="0 0 140 140" fill="none" stroke="#fff" stroke-width="4">
  <circle cx="70" cy="38" r="28"/><path d="M70 22 V54 M54 38 H86"/>
  <path d="M8 40 V86 L38 120 V136 M30 60 V92 L50 112"/>
  <path d="M132 40 V86 L102 120 V136 M110 60 V92 L90 112"/>
</svg>

<p class="service-text" style="left:119px;top:2733px">Plan every visit, match the right carer to each client and keep schedules current from one clear dashboard. Staff get instant updates on any device, so families always know who is coming and when care happens.</p>
<p class="service-text" style="left:474px;top:2733px">Plan every visit, match the right carer to each client and keep schedules current from one clear dashboard. Staff get instant updates on any device, so families always know who is coming and when care happens.</p>
<p class="service-text" style="left:839px;top:2733px">Plan every visit, match the right carer to each client and keep schedules current from one clear dashboard. Staff get instant updates on any device, so families always know who is coming and when care happens.</p>

<h2 class="contact-title">Contact Us</h2>
<p class="contact-text">Lorem ipsum dolor sit amet, consectetur adipiscing elit. Cras lacinia hendrerit leo tincidunt dapibus. Fusce efficitur sollicitu-din blandit. Phasellus dolor dolor, luctus tempus rhoncus eu, luctus non arcu. Ut purus arcu, consectetur id sem et, aliquet tincidunt diam.</p>
<p class="contact-phone">+1.555.014.2870</p>

<div class="field" style="top:3146px">Your name...</div>
<div class="field" style="top:3208px">Your email...</div>
<div class="field" style="top:3271px">Your phone...</div>
<div class="field tall" style="top:3331px">Your message...</div>
<div class="btn" style="left:555px;top:3445px;width:468px;height:38px">SEND</div>

<footer class="site-footer">
  <div class="brand footer-brand" style="left:30px;top:28px">
    <span class="brand-mark"></span>
    <span class="brand-name">VISITLINE</span>
  </div>
  <div class="footer-contact" style="left:725px;top:26px"><div class="label">Call Now!</div><div>+1.555.014.2870</div></div>
  <div class="footer-contact" style="left:857px;top:26px"><div>Email Us!</div><div>hello@visitline.co</div></div>
  <div class="btn" style="left:1031px;top:12px;width:135px;height:38px">Free Demo</div>
  <div class="footer-rule"></div>
  <div class="footer-col" style="left:32px">Lorem ipsum 1<br>Lorem ipsum 2<br>Lorem ipsum 3</div>
  <div class="footer-col" style="left:135px">Lorem ipsum 1<br>Lorem ipsum 2<br>Lorem ipsum 3</div>
  <div class="footer-col" style="left:238px">Lorem ipsum 1<br>Lorem ipsum 2<br>Lorem ipsum 3</div>
  <div class="footer-col" style="left:341px">Lorem ipsum 1<br>Lorem ipsum 2<br>Lorem ipsum 3</div>
  <div class="footer-col" style="left:445px">Lorem ipsum 1<br>Lorem ipsum 2<br>Lorem ipsum 3</div>
  <span class="social" style="left:1107px" aria-label="Social profile"></span>
  <span class="social" style="left:1143px" aria-label="Social profile"></span>
  <div class="legal">© 2020 All Rights Reserved &nbsp;&nbsp;&nbsp;&nbsp;&nbsp; Terms and Conditions | Privacy Policy | Cookie Policy</div>
</footer>

</body>
</html>
```